Webdesign für Hundeerziehungsberatung
Zielgruppe:
Hundehalter, die entweder einen Welpen angeschafft haben, ihren Hund ausbilden oder fördern wollen sowie Menschen mit einem 'Problemhund'.
Die Hundeerziehungsberatung bietet Hundehaltern die Erziehung im Einzelsetting und im Gruppensetting an.
Aufgabenstellung
die Farben sollen sich am Logo orientieren, gern noch eine Farbe dazu. Logo anbei, Bilder anbei. Flyer anbei
Sollten die Bilder ausreichen bitten wir um Auswahl bei pixel.morvani. Tool: Photoshop.
Der Kundin gefällt: https://www.pfotenlauf-brevik.de/

```html
<!DOCTYPE html>
<html lang="de">
<head>
<meta charset="utf-8">
<title>Hundeschule Spürsinn in Chemnitz</title>
<link href="https://fonts.googleapis.com/css2?family=Montserrat:wght@500;600;700&family=Arimo:wght@400;700&display=swap" rel="stylesheet">
<style>
:root{
  --brown:#7b7168;
  --brown-dark:#6b625a;
  --grey:#a9a6a7;
  --grey-light:#c9c5c2;
  --text:#7a7a7a;
  --line:#d9d6d4;
  --footer:#f2f2f2;
  --white:#ffffff;
}
*{margin:0;padding:0;box-sizing:border-box}
html,body{width:1200px;height:4689px;overflow:hidden;background:var(--white)}
body{font-family:"Arimo",Arial,sans-serif;color:var(--text);position:relative}
.abs{position:absolute}
h1,h2,h3,h4{font-family:"Montserrat",Helvetica,sans-serif;color:var(--brown);font-weight:600}

/* header */
.site-header{position:absolute;left:0;top:0;width:1200px;height:135px;background:var(--white);box-shadow:0 2px 6px rgba(0,0,0,.06);z-index:2}
.brand{position:absolute;left:92px;top:12px;display:flex;align-items:center;gap:10px}
.brand-mark{width:80px;height:80px;border-radius:50%;border:3px solid var(--brown)}
.brand-name{font-family:"Montserrat",sans-serif;font-weight:500;font-size:33px;color:var(--brown)}
.phone{position:absolute;right:74px;top:38px;display:flex;align-items:center;gap:8px;font-family:"Montserrat",sans-serif;font-size:20px;color:var(--brown)}
.main-nav{position:absolute;left:95px;top:106px;display:flex;font-family:"Montserrat",sans-serif;font-size:15.5px;color:var(--brown)}
.main-nav span{margin-right:28px}

/* hero */
.hero{position:absolute;left:0;top:135px;width:1200px;height:723px;background:linear-gradient(100deg,#b49a62 0%,#9d8a66 25%,#c9b07a 50%,#a89478 70%,#c7a46c 100%)}
.hero-blob{position:absolute;left:90px;top:292px;z-index:1}
.hero-title{position:absolute;left:128px;top:430px;width:360px;text-align:center;color:var(--white);font-family:"Montserrat",sans-serif;font-weight:700;font-size:38px;line-height:48px;text-transform:uppercase;z-index:2}

/* shared */
.section-title{font-size:32px;line-height:40px;text-transform:uppercase}
.body-text{font-size:19.5px;line-height:33px;text-align:justify}
.divider{position:absolute;left:0;width:1200px;height:30px;background:linear-gradient(to bottom,rgba(0,0,0,.07),rgba(0,0,0,0))}
.btn{display:inline-block;background:var(--grey);color:var(--white);font-family:"Montserrat",sans-serif;font-weight:700;font-size:13px;width:140px;height:38px;line-height:38px;text-align:center;border-radius:2px}

/* offers */
.intro{left:93px;top:952px;width:418px}
.intro .body-text{margin-top:24px}
.offers-head{left:0;top:1655px;width:1200px;text-align:center}
.offers-head p{font-size:19px;margin-top:20px}
.card{position:absolute;top:1857px;width:312px;height:498px;border:1.5px solid var(--line);text-align:center}
.card-photo{margin:7px;height:230px}
.card h3{font-size:21px;letter-spacing:1px;margin-top:22px}
.card p{font-size:15px;line-height:26px;margin:18px 18px 0}
.card .btn{margin-top:22px}

/* team */
.team{left:600px;top:2630px;width:524px}
.team h3{font-size:27px;font-weight:500;margin-top:40px}
.team .body-text{margin-top:32px}

/* testimonial */
.voices-head{left:0;top:3378px;width:1200px;text-align:center;font-size:35px;line-height:45px}
.quote-text{left:130px;top:3888px;width:960px;text-align:center;font-size:15px;line-height:35px}
.quote-name{display:block;font-weight:700;color:var(--brown);margin-top:2px}
.dots{left:570px;top:4110px;display:flex;gap:12px}
.dots i{width:12px;height:12px;border-radius:50%;background:var(--brown);opacity:.8}

/* footer */
.site-footer{position:absolute;left:0;top:4200px;width:1200px;height:489px;background:var(--footer)}
.contact{position:absolute;left:92px;top:110px}
.contact h4,.newsletter h4{font-size:36px;font-weight:500}
.contact .sub{font-size:17px;margin-top:4px}
.contact-row{display:flex;align-items:center;gap:16px;font-size:17px;margin-top:16px}
.social{display:flex;gap:22px;margin-top:24px}
.social i{width:40px;height:40px;border-radius:50%;background:var(--brown)}
.newsletter{position:absolute;left:700px;top:110px;width:426px}
.newsletter p{font-size:17px;line-height:32px;text-align:justify;margin-top:14px}
.signup{display:flex;margin-top:16px;height:58px}
.signup .field{flex:1;background:var(--grey-light);color:var(--white);font-size:14px;padding:22px 14px}
.signup .go{width:68px;background:var(--brown);display:flex;align-items:center;justify-content:center}
</style>
</head>
<body>

<header class="site-header">
  <div class="brand"><span class="brand-mark"></span><span class="brand-name">PfotenWerk</span></div>
  <div class="phone">
    <svg width="22" height="26" viewBox="0 0 22 26" fill="none" stroke="#7b7168" stroke-width="1.8"><path d="M5 2l4 6-3 3c1 4 4 8 8 10l3-3 5 4-3 3C9 24 2 13 2 5z"/></svg>
    012-30987654
  </div>
  <nav class="main-nav">
    <span>Home</span><span>Erstgespräch</span><span>Erziehung im Einzelsetting</span><span>Erziehung im Gruppensetting</span><span style="margin-left:6px">Unternehmen</span><span>Veranstaltungen</span><span>Kontakt</span>
  </nav>
</header>

<section class="hero" role="img" aria-label="Foto: Trainerin kniet im herbstlichen Gras vor einem schwarz-weißen Hund"></section>
<svg class="hero-blob" width="420" height="365" viewBox="0 0 420 365">
  <path d="M150 10C80 25 10 120 5 200 0 270 60 330 150 345 250 360 330 320 320 250 310 170 250 0 150 10Z" fill="#9b9896"/>
  <path d="M183 5C260 0 330 80 380 180 420 260 430 340 330 355 230 365 120 350 70 290 20 230 40 100 100 45 130 18 160 7 183 5Z" fill="#7b7168"/>
</svg>
<h1 class="hero-title">Hundeschule Spürsinn in Chemnitz</h1>

<!-- intro -->
<div class="abs intro">
  <h2 class="section-title" style="font-size:31px">Spürsinn<br>vielfältige Angebote<br>warten auf dich</h2>
  <p class="body-text">Lorem ipsum dolor sit amet, consectetuer adipiscing elit. Aenean commodo ligula eget dolor. Aenean massa. Cum sociis natoque penatibus et magnis dis parturient montes, nascetur ridiculus mus. Donec quam felis, ultricies nec, pellentesque eu, pretium quis, sem. Nulla consequat massa quis enim. Donec pede justo, fringilla vel, aliquet nec, vulputate eget, arcu. In enim justo, rhoncus ut, imperdiet a, venenatis vitae, justo. Nullam dictum felis eu pede mollis pretium. Integer tincidunt.</p>
</div>
<svg class="abs" style="left:605px;top:1005px" width="510" height="440" viewBox="0 0 510 440" role="img" aria-label="Foto: zwei Hunde spielen auf einer Wiese">
  <defs><linearGradient id="gIntro" x1="0" y1="0" x2="0" y2="1"><stop offset="0" stop-color="#8fa9c9"/><stop offset=".45" stop-color="#8a8a6e"/><stop offset="1" stop-color="#5f8a3a"/></linearGradient></defs>
  <path d="M120 130C60 170 0 250 5 330 10 400 80 430 170 425 260 420 300 380 250 330 200 280 180 100 120 130Z" fill="#c9c4bf"/>
  <path d="M250 10C170 10 90 110 60 200 30 290 90 380 200 420 320 460 450 430 495 360 530 300 450 190 390 110 350 50 310 10 250 10Z" fill="url(#gIntro)"/>
</svg>

<div class="divider" style="top:1585px"></div>

<!-- offers -->
<div class="abs offers-head">
  <h2 class="section-title" style="line-height:40px">Spürsinn<br>vielfältige Angebote warten</h2>
  <p>Lorem ipsum dolor sit amet, consectetuer adipiscing elit.</p>
</div>
<article class="card" style="left:92px">
  <div class="card-photo" role="img" aria-label="Foto: Hund liegt im Gras" style="background:linear-gradient(160deg,#6e8e3e,#2c2c2a 50%,#7ea24a)"></div>
  <h3>EINZELCOACHING</h3>
  <p>Lorem ipsum dolor sit amet, consectetuer adipiscing elit. Aenean commodo ligula eget dolor. Aenean massa. Integer tincidunt.</p>
  <span class="btn">Mehr Wissen</span>
</article>
<article class="card" style="left:452px">
  <div class="card-photo" role="img" aria-label="Foto: drei Hunde toben auf der Wiese" style="background:linear-gradient(180deg,#8fa56a,#6f9a3c 40%,#3a3a32 70%,#7ea24a)"></div>
  <h3>EINZELCOACHING</h3>
  <p>Lorem ipsum dolor sit amet, consectetuer adipiscing elit. Aenean commodo ligula eget dolor. Aenean massa. Integer tincidunt.</p>
  <span class="btn">Mehr Wissen</span>
</article>
<article class="card" style="left:812px">
  <div class="card-photo" role="img" aria-label="Foto: Hund liegt im Gras" style="background:linear-gradient(160deg,#6e8e3e,#2c2c2a 50%,#7ea24a)"></div>
  <h3>EINZELCOACHING</h3>
  <p>Lorem ipsum dolor sit amet, consectetuer adipiscing elit. Aenean commodo ligula eget dolor. Aenean massa. Integer tincidunt.</p>
  <span class="btn">Mehr Wissen</span>
</article>

<div class="divider" style="top:2480px"></div>

<!-- team -->
<svg class="abs" style="left:62px;top:2695px" width="510" height="430" viewBox="0 0 510 430" role="img" aria-label="Foto: Trainerin mit schwarz-weißem Hund im Herbstgras">
  <defs><linearGradient id="gTeam" x1="0" y1="0" x2="1" y2="1"><stop offset="0" stop-color="#c4a46a"/><stop offset=".5" stop-color="#b9b7b2"/><stop offset="1" stop-color="#8d7f62"/></linearGradient></defs>
  <path d="M110 140C50 190 0 270 10 340 20 400 90 430 170 420 250 410 270 370 220 320 170 270 170 90 110 140Z" fill="#c9c4bf"/>
  <path d="M250 10C170 10 90 110 60 200 30 290 90 380 200 415 320 450 450 430 495 360 530 300 450 190 390 110 350 50 310 10 250 10Z" fill="url(#gTeam)"/>
</svg>
<div class="abs team">
  <h2 class="section-title" style="font-size:35px">Das Team</h2>
  <h3>MARA LINDHOLM</h3>
  <p class="body-text">Lorem ipsum dolor sit amet, consectetuer adipiscing elit. Aenean commodo ligula eget dolor. Aenean massa. Cum sociis natoque penatibus et magnis dis parturient montes, nascetur ridiculus mus. Donec quam felis, ultricies nec, pellentesque eu, pretium quis, sem. Nulla consequat massa quis enim. Donec pede justo, fringilla vel, aliquet nec, vulputate eget, arcu. In enim justo, rhoncus ut, imperdiet a, venenatis vitae, justo. Nullam dictum felis eu pede mollis pretium. Integer tincidunt.</p>
</div>

<div class="divider" style="top:3255px"></div>

<!-- testimonial -->
<h2 class="abs section-title voices-head">Den Weg als Ziel sehe<br>Kundenstimmen</h2>
<svg class="abs" style="left:432px;top:3505px" width="350" height="300" viewBox="0 0 350 300" role="img" aria-label="Foto: Mann gibt einem hellen Retriever High Five">
  <defs><linearGradient id="gVoice" x1="0" y1="0" x2="1" y2="0"><stop offset="0" stop-color="#6d6a66"/><stop offset=".5" stop-color="#d8cfc4"/><stop offset="1" stop-color="#d1a870"/></linearGradient></defs>
  <path d="M60 110C20 150 0 210 20 250 40 290 110 300 170 290 120 260 110 160 60 110Z" fill="#a9a6a7"/>
  <path d="M180 5C120 5 60 90 40 160 25 230 80 285 170 290 260 295 345 250 345 190 345 120 250 5 180 5Z" fill="url(#gVoice)"/>
</svg>
<svg class="abs" style="left:140px;top:3802px" width="80" height="64" viewBox="0 0 80 64">
  <path d="M2 64V34C2 14 12 4 30 0v10c-9 3-13 9-13 16h16v38zM44 64V34C44 14 54 4 72 0v10c-9 3-13 9-13 16h16v38z" fill="#7b7168"/>
</svg>
<p class="abs quote-text">Danke, lieber Jonas, für deine Ruhe, deine Geduld und Ausgeglichenheit sowie die vielen guten Tipps aus einer für mich anfangs ungewohnten Perspektive. Heute bin ich froh, dass ich mich darauf eingelassen habe, neue Wege in der Hundeerziehung zu gehen. Aus meiner hyperaktiven Goldendoodle-Hündin Inka ist eine ausgeglichene, zufrieden wirkende Begleiterin geworden. Auch unsere Verwandten, Freunde und Nachbarn bestätigen den charakterlichen Wandel seit Juni 2016 immer wieder. Danke!<span class="quote-name">Greta Wendlandt</span></p>
<div class="abs dots"><i></i><i></i><i></i></div>

<!-- footer -->
<footer class="site-footer">
  <div class="contact">
    <h4>Kontakt</h4>
    <p class="sub">Hundeschule Spürsinn</p>
    <div class="contact-row"><svg width="30" height="30" viewBox="0 0 30 30" fill="none" stroke="#7b7168" stroke-width="1.6"><path d="M15 28C8 19 5 15 5 11a10 10 0 0 1 20 0c0 4-3 8-10 17z"/><circle cx="15" cy="11" r="3.5"/></svg>Aenean commodo ligula eget dolor.</div>
    <div class="contact-row"><svg width="30" height="30" viewBox="0 0 22 26" fill="none" stroke="#7b7168" stroke-width="1.6"><path d="M5 2l4 6-3 3c1 4 4 8 8 10l3-3 5 4-3 3C9 24 2 13 2 5z"/></svg>0112 – 310 442 718</div>
    <div class="contact-row"><svg width="30" height="30" viewBox="0 0 30 30" fill="none" stroke="#7b7168" stroke-width="1.8"><circle cx="15" cy="15" r="4.5"/><path d="M19.5 11v6c0 3 4.5 3 4.5-2a9 9 0 1 0-4 7.5"/></svg>info@spuersinn-hunde.de</div>
    <div class="social" aria-label="Soziale Netzwerke"><i></i><i></i><i></i></div>
  </div>
  <div class="newsletter">
    <h4>Unser Newsletter</h4>
    <p>Lorem ipsum dolor sit amet, consectetuer adipiscing elit. Aenean commodo ligula eget dolor.</p>
    <div class="signup">
      <div class="field">Email</div>
      <div class="go"><svg width="18" height="26" viewBox="0 0 18 26" fill="none" stroke="#fff" stroke-width="2.5"><path d="M4 3l10 10L4 23"/></svg></div>
    </div>
  </div>
</footer>

</body>
</html>
```